Design our Hot Cup Jacket / Coffee Sleeve

I am looking for a chic and eye catchy design (using our logo) to put on our coffee cup sleeve to include our Cafe and our coffee truck. We do not need separate design. Both the Cafe and the coffee truck can be represented on the same Coffee Sleeve design. I have provided both logos; one for our Cafe which is called Marigold Lane Cafe & Coffee Bar and the other logo is for our coffee truck which is called The Little Kettle. We would like a back and front design. Can you please include our instragram - marigoldlanecafexq and thelittlekettlexq

Our Cafe serves breakfast and lunch consisting of full breakfast (pancakes, eggs, bacon, home fries, omeletts etc), lunch (made to order sandwiches and wraps, homemade soups, salads) and freshly baked scones, muffins, pies and cakes. I have also attached a few pictures of the Cafe food, outside on the deck of our Cafe and the Coffee Truck.

Target Market(s)

customers

Industry/Entity Type

Cafe, restaurant, coffee truck

Requirements
Must have
• logo, Instagram name, chic and classy, our logo color
Nice to have
• pictures

```html
<!DOCTYPE html>
<html lang="en">
<head>
<meta charset="utf-8">
<title>Cup Sleeve – The Little Kettle &amp; Marigold Lane</title>
<link rel="stylesheet" href="https://fonts.googleapis.com/css2?family=Oswald:wght@400;600&family=Poppins:wght@800&display=swap">
<style>
  :root {
    --espresso: #50262a;
    --latte: #dcae93;
    --blush: #e6c3b3;
    --ink: #1f1515;
    --cocoa: #4a2b2c;
    --bean: #5a3233;
    --bean-soft: #b98a78;
  }
  * { margin: 0; padding: 0; box-sizing: border-box; }
  html, body { width: 1200px; height: 1121px; overflow: hidden; background: var(--blush); }
  .canvas { position: relative; width: 1200px; height: 1121px; }

  /* Flat sleeve artwork */
  .sleeve-flat { position: absolute; left: 0; top: 0; width: 1200px; height: 379px; background: var(--espresso); }
  .sleeve-flat__body { position: absolute; left: 0; top: 40px; width: 1200px; height: 300px; background: var(--latte); }
  .brand { position: absolute; top: 0; height: 300px; text-align: center; }
  .brand--truck { left: 0; width: 540px; }
  .brand--cafe { left: 580px; width: 600px; }
  .brand__art {
    position: absolute; left: 175px; top: 37px; width: 190px; height: 117px;
    border-radius: 60px;
    background: radial-gradient(ellipse at center, var(--bean) 0%, var(--bean-soft) 75%, var(--latte) 100%);
  }
  .brand__name {
    position: absolute; left: 0; right: 0;
    font-family: "Oswald", sans-serif; font-weight: 600;
    color: var(--ink); letter-spacing: 0.5px; line-height: 1;
  }
  .brand--truck .brand__name { top: 160px; font-size: 50px; }
  .brand--cafe .brand__name { top: 88px; font-size: 42px; line-height: 1.08; }
  .handle {
    position: absolute; left: 0; right: 0; top: 252px;
    display: flex; align-items: center; justify-content: center; gap: 8px;
    font-family: "Oswald", sans-serif; font-weight: 400; font-size: 31px;
    color: var(--cocoa); line-height: 1;
  }
  .handle__dot { width: 24px; height: 24px; border: 3px solid var(--cocoa); border-radius: 6px; }

  /* Section bands */
  .section-band {
    position: absolute; left: 0; width: 1200px; background: var(--espresso);
    font-family: "Poppins", sans-serif; font-weight: 800; color: var(--latte);
  }
  .section-band--design { top: 380px; height: 127px; text-align: center; font-size: 88px; line-height: 127px; letter-spacing: 1px; }
  .section-band--sides { top: 957px; height: 164px; font-size: 90px; }
  .side-label { position: absolute; top: 34px; line-height: 1; }
  .side-label--front { left: 158px; }
  .side-label--back { left: 848px; }

  /* Front / back sleeve panels */
  .panel { position: absolute; top: 676px; width: 205px; height: 154px; background: var(--espresso); }
  .panel--front { left: 201px; }
  .panel--back { left: 801px; }
  .panel__body {
    position: absolute; left: 0; top: 15px; width: 205px; height: 124px; background: var(--latte);
    text-align: center;
  }
  .panel__art {
    position: absolute; left: 64px; top: 14px; width: 70px; height: 42px; border-radius: 22px;
    background: radial-gradient(ellipse at center, var(--bean) 0%, var(--bean-soft) 75%, var(--latte) 100%);
  }
  .panel__name {
    position: absolute; left: 0; right: 0;
    font-family: "Oswald", sans-serif; font-weight: 600; color: var(--ink); line-height: 1;
  }
  .panel--front .panel__name { top: 61px; font-size: 17px; }
  .panel--back .panel__name { top: 35px; font-size: 15px; line-height: 1.1; }
  .panel__handle {
    position: absolute; left: 0; right: 0; top: 104px;
    display: flex; align-items: center; justify-content: center; gap: 4px;
    font-family: "Oswald", sans-serif; font-size: 11px; color: var(--cocoa); line-height: 1;
  }
  .panel__handle .handle__dot { width: 9px; height: 9px; border-width: 1.5px; border-radius: 2px; }
</style>
</head>
<body>
<div class="canvas">
  <section class="sleeve-flat">
    <div class="sleeve-flat__body">
      <div class="brand brand--truck">
        <div class="brand__art" role="img" aria-label="Illustration area for The Little Kettle coffee truck artwork"></div>
        <p class="brand__name">The Little Kettle</p>
        <p class="handle"><span class="handle__dot"></span>thelittlekettlexq</p>
      </div>
      <div class="brand brand--cafe">
        <p class="brand__name">Marigold Lane<br>Cafe &amp; Coffee Bar</p>
        <p class="handle"><span class="handle__dot"></span>marigoldlanecafexq</p>
      </div>
    </div>
  </section>

  <div class="section-band section-band--design">DESIGN</div>

  <div class="panel panel--front">
    <div class="panel__body">
      <div class="panel__art" role="img" aria-label="Illustration area for The Little Kettle coffee truck artwork"></div>
      <p class="panel__name">The Little Kettle</p>
      <p class="panel__handle"><span class="handle__dot"></span>thelittlekettlexq</p>
    </div>
  </div>
  <div class="panel panel--back">
    <div class="panel__body">
      <p class="panel__name">Marigold Lane<br>Cafe &amp; Coffee Bar</p>
      <p class="panel__handle"><span class="handle__dot"></span>marigoldlanecafexq</p>
    </div>
  </div>

  <div class="section-band section-band--sides">
    <span class="side-label side-label--front">FRONT</span>
    <span class="side-label side-label--back">BACK</span>
  </div>
</div>
</body>
</html>
```